New business card for civil engineering company - "Keystone Audit"

We need a business card designed for our new structural engineering company.

The company name is "Keystone Audit" logo files attached.

We would like the following:
* Two-sided card
* Simple design

Information to be placed on the card:
Name - Marcus Dellow
Job Title - Director / Structural Engineer
Credentials - BEng(Hons), CPEng, CMengNZ, IntPE(NZ)
Email - marcus.dellow@keystoneaudit.co.nz
mobile - 0219364058
website - www.keystoneaudit.co.nz

```html
<!DOCTYPE html>
<html lang="en">
<head>
<meta charset="utf-8">
<title>Keystone Audit – Business Card</title>
<link rel="stylesheet" href="https://fonts.googleapis.com/css2?family=Michroma&family=Saira:wght@400;500;600&display=swap">
<style>
  :root {
    --page-bg: #e8eaed;
    --navy: #063a61;
    --navy-deep: #042c4b;
    --brand-muted: #2d6ea3;
    --sky: #4f8ec6;
    --ink-blue: #1f67ad;
    --ink-grey: #4a4f55;
    --ink-soft: #7a8088;
    --card-white: #f7f8f9;
  }
  * { margin: 0; padding: 0; box-sizing: border-box; }
  html, body { width: 1200px; height: 600px; overflow: hidden; }
  body {
    background: var(--page-bg);
    font-family: "Saira", sans-serif;
    position: relative;
  }
  .card {
    position: absolute;
    top: 150px;
    width: 520px;
    height: 300px;
    border-radius: 4px;
    overflow: hidden;
    box-shadow: 0 6px 18px rgba(0,0,0,0.18);
  }
  .card--front { left: 50px; background: var(--navy); }
  .card--back  { left: 630px; background: var(--card-white); }

  .wordmark {
    display: flex;
    align-items: center;
    gap: 10px;
    font-family: "Saira", sans-serif;
    font-weight: 500;
    letter-spacing: 0.12em;
    text-transform: uppercase;
    white-space: nowrap;
  }
  .wordmark__square { width: 14px; height: 14px; flex: none; }
  .card--front .wordmark {
    position: absolute; left: 50%; top: 50%;
    transform: translate(-50%, -50%);
    font-size: 24px; color: var(--brand-muted);
  }
  .card--front .wordmark__square { background: var(--brand-muted); }

  .card--back .wordmark {
    position: absolute; left: 28px; top: 176px;
    font-size: 17px; color: var(--ink-grey);
  }
  .card--back .wordmark__square { background: var(--sky); width: 12px; height: 12px; }

  .contact-block {
    position: absolute; left: 248px; top: 92px;
  }
  .person-name {
    font-family: "Michroma", sans-serif;
    font-size: 19px;
    color: var(--ink-blue);
    letter-spacing: 0.04em;
    white-space: nowrap;
  }
  .person-role {
    margin-top: 4px;
    font-size: 12.5px;
    color: var(--ink-grey);
    letter-spacing: 0.06em;
  }
  .person-credentials {
    font-size: 8.5px;
    color: var(--ink-soft);
    letter-spacing: 0.08em;
  }
  .contact-list { list-style: none; margin-top: 14px; }
  .contact-list li {
    display: flex; align-items: center; gap: 9px;
    font-size: 13.5px; color: var(--ink-grey);
    letter-spacing: 0.05em; line-height: 23px;
    white-space: nowrap;
  }
  .contact-list svg { width: 13px; height: 13px; flex: none; }
  .card-bands { position: absolute; left: 0; bottom: 0; width: 520px; height: 30px; }
</style>
</head>
<body>
  <section class="card card--front" aria-label="Card front">
    <div class="wordmark"><span class="wordmark__square"></span>Keystone Audit</div>
  </section>

  <section class="card card--back" aria-label="Card back">
    <div class="wordmark"><span class="wordmark__square"></span>Keystone Audit</div>

    <div class="contact-block">
      <h1 class="person-name">Marcus Dellow</h1>
      <p class="person-role">Director / Structural Engineer</p>
      <p class="person-credentials">BEng(Hons), CPEng, CMengNZ, IntPE(NZ)</p>
      <ul class="contact-list">
        <li>
          <svg viewBox="0 0 14 14" aria-hidden="true"><circle cx="7" cy="7" r="7" fill="#1f67ad"/><path d="M4.6 3.6l1.3 1.4-.7.9c.5 1 1.3 1.8 2.3 2.3l.9-.7 1.4 1.3-.8 1.2C6.4 9.8 4.2 7.6 3.8 4.4z" fill="#fff"/></svg>
          0219364058
        </li>
        <li>
          <svg viewBox="0 0 14 14" aria-hidden="true"><circle cx="7" cy="7" r="7" fill="#1f67ad"/><rect x="3.5" y="4.6" width="7" height="4.8" fill="none" stroke="#fff" stroke-width="1"/><path d="M3.5 4.6L7 7.4l3.5-2.8" fill="none" stroke="#fff" stroke-width="1"/></svg>
          marcus.dellow@keystoneaudit.co.nz
        </li>
        <li>
          <svg viewBox="0 0 14 14" aria-hidden="true"><circle cx="7" cy="7" r="7" fill="#1f67ad"/><circle cx="7" cy="7" r="3.8" fill="none" stroke="#fff" stroke-width=".9"/><ellipse cx="7" cy="7" rx="1.6" ry="3.8" fill="none" stroke="#fff" stroke-width=".9"/><path d="M3.2 7h7.6" stroke="#fff" stroke-width=".9"/></svg>
          www.keystoneaudit.co.nz
        </li>
      </ul>
    </div>

    <svg class="card-bands" viewBox="0 0 520 30" preserveAspectRatio="none" aria-hidden="true">
      <polygon points="0,22 300,22 290,30 0,30" fill="#063a61"/>
      <polygon points="318,12 520,12 520,30 306,30" fill="#4f8ec6"/>
    </svg>
  </section>
</body>
</html>
```